Land Buying Company Needs Letterhead for Direct Mail Marketing to Land Owners

We are looking for a professional letterhead that we will be including in our direct mail marketing. We will be sending this to land owners who may be interested in selling or purchasing land.

The letterhead needs to be editable. Headers and footers would look nice, but we are open. We would want it to include our address, website, phone, and email info. For right now the address to use for design purposes would the following:

Address: 415 Bramwell Avenue #600
Dallas, TX 75219
Website - www.quillridgeacres.example
Email - info@quillridgeacres.example
Phone - 866-402-ACRE

I have attached our logo zip file that we just had done on Pixel Guild. Let me know what questions you have, and thank you.

```html
<!DOCTYPE html>
<html lang="en">
<head>
<meta charset="utf-8">
<title>Quillridge Acres Letterhead</title>
<link href="https://fonts.googleapis.com/css2?family=Open+Sans:wght@400;600&family=Montserrat:wght@600&family=Lato:wght@400;700&display=swap" rel="stylesheet">
<style>
  :root {
    --paper: #ffffff;
    --ink: #4a4a4a;
    --ink-dark: #333333;
    --brand-green: #8cc63f;
    --brand-dark: #3f5f1f;
    --footer-green: #2f5a14;
    --watermark: #efefeb;
  }
  html, body {
    margin: 0;
    padding: 0;
    width: 1040px;
    height: 1200px;
    overflow: hidden;
    background: var(--paper);
  }
  .letterhead {
    position: relative;
    width: 1040px;
    height: 1200px;
    background: var(--paper);
    font-family: "Open Sans", sans-serif;
    color: var(--ink);
  }
  .brand {
    position: absolute;
    top: 26px;
    left: 0;
    width: 100%;
    display: flex;
    justify-content: center;
    align-items: center;
    gap: 16px;
  }
  .brand-mark {
    width: 60px;
    height: 60px;
    border-radius: 50%;
    background: var(--brand-dark);
  }
  .brand-name {
    font-family: "Open Sans", sans-serif;
    font-weight: 600;
    font-size: 38px;
    letter-spacing: 1px;
    color: var(--brand-green);
  }
  .watermark {
    position: absolute;
    left: 246px;
    top: 272px;
    width: 580px;
    height: 580px;
    border-radius: 50%;
    background: var(--watermark);
  }
  .letter-body {
    position: absolute;
    left: 97px;
    top: 355px;
    width: 840px;
    font-size: 15.5px;
    line-height: 30px;
  }
  .salutation { margin: 0 0 23px; }
  .letter-body p.paragraph {
    margin: 0 0 24px;
    text-align: justify;
    hyphens: auto;
  }
  .closing { position: absolute; left: 97px; top: 808px; margin: 0; font-size: 15.5px; }
  .signatory-name {
    position: absolute; left: 97px; top: 890px; margin: 0;
    font-size: 19px; font-weight: 600; color: var(--ink-dark);
  }
  .signatory-title { position: absolute; left: 97px; top: 922px; margin: 0; font-size: 15.5px; }
  .footer {
    position: absolute;
    left: 113px;
    top: 1130px;
    width: 813px;
    font-family: "Lato", sans-serif;
    color: var(--footer-green);
    text-align: center;
    font-size: 18.5px;
  }
  .footer-address { margin: 0 0 4px; }
  .footer-rule { height: 2px; background: var(--brand-green); }
  .footer-contacts { margin: 6px 0 0; color: var(--ink-dark); }
  .footer-contacts b { color: var(--footer-green); }
  .footer-web { color: var(--footer-green); }
</style>
</head>
<body>
<main class="letterhead">
  <header class="brand">
    <div class="brand-mark"></div>
    <div class="brand-name">QUILLRIDGE ACRES</div>
  </header>

  <div class="watermark"></div>

  <section class="letter-body">
    <p class="salutation">Dear Mr.XYZABC</p>
    <p class="paragraph">Lorem Ipsum has been the industry's standard dummy text ever since the 1500s, when an unknown printer took a galley of type and scrambled it to make a type specimen book. It has survived not only five centuries, but also the leap into electronic typesetting, remaining essentially unchanged. It was popularised in the 1960s with the release of Letraset sheets containing Lorem Ipsum passages, and more recently with desktop publishing software like Aldus PageMaker including versions of Lorem Ipsum.</p>
    <p class="paragraph">Lorem Ipsum is simply dummy text of the printing and typesetting industry. Lorem Ipsum has been the industry's standard dummy text ever since the 1500s, when an unknown printer took a galley of type and scrambled it to make a type specimen book.</p>
    <p class="paragraph">It has survived not only five centuries, but also the leap into electronic typesetting, remaining essentially unchanged. It was popularised in the 1960s with the release of Letraset sheets containing Lorem IpsumIpsum passages.</p>
  </section>

  <p class="closing">Yours Sincerely</p>
  <p class="signatory-name">Marcus Hale</p>
  <p class="signatory-title">Managing Director</p>

  <footer class="footer">
    <p class="footer-address">415 Bramwell Avenue #600 Dallas, TX 75219</p>
    <div class="footer-rule"></div>
    <p class="footer-contacts"><b>P :</b> 866-402-ACRE &nbsp;| <b>E :</b> info@quillridgeacres.example | <span class="footer-web">www.quillridgeacres.example</span></p>
  </footer>
</main>
</body>
</html>
```